One page informative flyer for Florist

We are looking for a simple one page flyer. We are a florist who sell flowers, and commemorative t-shirts at graduation ceremonies, and need a flyer that can be given out to students so that they will know what is available on site. Further, we want the flyer to be editable (ie. a word template, or some other program), so that we can change the schools name, and change small bits of the copy easily.

What we are really looking for is a simple template, but we need 4 iterations of the flyer. With each of our two logos, I will need a flyer for t-shirts, and a flyer for flowers. Making 4 total. Please see breakdown below as explanation:

1, Tassel Lane Flowers logo - flyer for flowers
2. Tassel Lane Flowers logo - flyer for shirts
3. Brightmarch Flowers logo - flyer for flowers
4. Brightmarch Flowers logo - flyer for shirts

Please see logos for Tassel Lane Flowers and Brightmarch Flowers attached, as well as a picture of flowers and of the shirts. Feel free to use those images or stock images.

Here is the copy:

Flowers - A variety floral arrangements will be available for purchase at our stand, located conveniently at the graduation ceremony. You can browse our selection & pre-order ahead of time at: www.brightmarchflowers-example.com/index,php/test

T-Shirts - Commerative T-Shirts displaying all of the students names will be available for purchase at our stand, located conveniently at the graduation ceremony. You can pre-order ahead of time to guarantee your choice of size at: www.brightmarchflowers-example.com/index.php/test

```html
<!DOCTYPE html>
<html lang="en">
<head>
<meta charset="utf-8">
<title>Brightmarch Flowers – Graduation Flyer</title>
<link rel="stylesheet" href="https://fonts.googleapis.com/css2?family=Oswald:wght@500&family=Arimo:wght@400;700&display=swap">
<style>
  :root {
    --paper: #eef2d0;
    --teal: #235864;
    --leaf: #7b9b3b;
    --ink: #1f5a66;
    --link: #cf3440;
    --white: #ffffff;
  }
  * { margin: 0; padding: 0; box-sizing: border-box; }
  html, body { width: 851px; height: 1200px; overflow: hidden; background: var(--paper); }
  .flyer { position: relative; width: 851px; height: 1200px; background: var(--paper); overflow: hidden; }

  .school-block {
    position: absolute; left: 0; top: 0; width: 263px; height: 370px;
    background: var(--teal);
  }
  .school-name {
    position: absolute; left: 62px; top: 170px;
    font-family: "Arimo", Arial, sans-serif; font-weight: 700;
    font-size: 27px; letter-spacing: 0.5px; color: var(--white);
  }
  .header-rule {
    position: absolute; left: 263px; top: 370px; width: 588px; height: 8px;
    background: var(--teal);
  }

  .brand {
    position: absolute; left: 330px; top: 82px; width: 510px;
    font-family: "Oswald", "Arial Narrow", sans-serif; font-weight: 500;
    color: var(--leaf); font-size: 92px; line-height: 96px;
  }
  .brand-line { display: block; }
  .brand-line--second { text-align: right; }

  .gallery {
    position: absolute; left: 76px; top: 428px;
    display: grid; grid-template-columns: repeat(3, 187px);
    column-gap: 66px; row-gap: 45px;
  }
  .gallery-tile {
    width: 187px; height: 156px; border-radius: 9px;
    border: 2px solid var(--teal);
  }
  .tile-yellow { background: radial-gradient(ellipse at 55% 55%, #e9c22a 0%, #d9a92b 40%, #8a6a3c 100%); }
  .tile-red    { background: radial-gradient(ellipse at 55% 55%, #c8232b 0%, #a81d24 40%, #7a5438 100%); }
  .tile-roses  { background: linear-gradient(160deg, #3d7a35 0%, #c3202a 35%, #b0151f 100%); }
  .tile-pink   { background: radial-gradient(ellipse at 55% 55%, #f0a3b3 0%, #dd8b9e 40%, #8c6a48 100%); }
  .tile-cream  { background: radial-gradient(ellipse at 55% 55%, #f6f0dc 0%, #e3dcc2 40%, #8c6a48 100%); }
  .tile-stems  { background: linear-gradient(180deg, #f2f2f0 0%, #c21d27 30%, #3f7d36 75%, #e8efe6 100%); }

  .copy {
    position: absolute; left: 78px; top: 823px; width: 690px;
    font-family: "Arimo", Arial, sans-serif; font-size: 28.5px; line-height: 36px;
    color: var(--ink); text-align: justify;
  }
  .web-address {
    position: absolute; left: 78px; top: 1017px;
    font-family: "Arimo", Arial, sans-serif; font-weight: 700;
    font-size: 27px; color: var(--link);
  }
</style>
</head>
<body>
<main class="flyer">
  <div class="school-block"><span class="school-name">SCHOOL</span></div>
  <div class="header-rule"></div>

  <h1 class="brand">
    <span class="brand-line">Brightmarch</span>
    <span class="brand-line brand-line--second">Flowers</span>
  </h1>

  <section class="gallery">
    <div class="gallery-tile tile-yellow" role="img" aria-label="Photo of a bouquet of yellow roses wrapped in paper"></div>
    <div class="gallery-tile tile-red" role="img" aria-label="Photo of a bouquet of red roses wrapped in paper"></div>
    <div class="gallery-tile tile-roses" role="img" aria-label="Close-up photo of red roses with green leaves"></div>
    <div class="gallery-tile tile-pink" role="img" aria-label="Photo of a bouquet of pink roses wrapped in paper"></div>
    <div class="gallery-tile tile-cream" role="img" aria-label="Photo of a bouquet of white roses wrapped in paper"></div>
    <div class="gallery-tile tile-stems" role="img" aria-label="Photo of long-stemmed red roses"></div>
  </section>

  <p class="copy">A variety floral arrangements will be available for purchase at our stand, located conveniently at the graduation ceremony. You can browse our selection &amp; pre-order ahead of time at:</p>
  <p class="web-address">www.brightmarchflowers-example.com</p>
</main>
</body>
</html>
```